Presentation Flyer for Married Couple at night separate business owners by day

I would like a flyer to use to advertise free presentations put on by husband and I. I (Renata Volkhaven) am an estate planning attorney that works for PWR Law. My husband (Dan Volkhaven) is a financial planner that works for Quelmora Financial Planning. Would love it to be funny but serious. At night we are a married couple of 4 children, by day we individually work with people helping them protect their assets and their families.
Goal is for this to be used for multiple events.
Things to include: Food will be provided, Raffle for $500 off an Estate Plan Package
Topics to be covered in Seminar:
Estate & Financial Planning Essentials

Protect Your Future
Build a strong financial foundation with emergency funds, retirement planning, and smart investment strategies that match your goals.

Secure Your Legacy
Learn about wills, trusts, and powers of attorney - the essential documents everyone needs to protect their family's future.

Guard Your Assets
Understand the right insurance coverage to protect yourself and your loved ones, from life insurance to long-term care options.

Transfer Wealth Wisely
Discover tax-efficient strategies for passing assets to the next generation and making the most of your charitable giving.

```html
<!DOCTYPE html>
<html lang="en">
<head>
<meta charset="utf-8">
<title>Estate &amp; Financial Planning Essentials</title>
<link rel="stylesheet" href="https://fonts.googleapis.com/css2?family=Oswald:wght@300;400;500;600;700&display=swap">
<style>
  :root {
    --navy: #0b4a87;
    --navy-deep: #0a4682;
    --white: #ffffff;
    --page-bg: #e9eaec;
    --ink: #1b1b1b;
    --logo-teal: #1f6f63;
    --photo-a: #8a5a48;
    --photo-b: #2b3448;
  }
  * { box-sizing: border-box; margin: 0; padding: 0; }
  html, body {
    width: 1199px; height: 1200px; overflow: hidden;
    background: var(--page-bg);
    font-family: "Oswald", "Arial Narrow", sans-serif;
  }
  .flyer {
    position: absolute; left: 203px; top: 40px;
    width: 792px; height: 1120px;
    background: var(--white);
    overflow: hidden;
  }
  .brand {
    position: absolute; display: flex; align-items: center; gap: 10px;
    font-weight: 600; line-height: 1;
  }
  .brand-financial {
    left: 48px; top: 56px; color: var(--logo-teal);
    font-size: 22px; line-height: 24px; text-transform: uppercase; letter-spacing: 0.5px;
  }
  .brand-law { left: 262px; top: 70px; color: var(--navy); font-size: 32px; line-height: 40px; }
  .brand-mark { width: 22px; height: 22px; background: currentColor; flex: none; }
  .accent-bar {
    position: absolute; left: 626px; top: 0; width: 93px; height: 178px;
    background: var(--navy);
  }
  .speaker-photo {
    position: absolute; left: 466px; top: 171px; width: 326px; height: 426px;
    background: linear-gradient(160deg, var(--photo-a) 0%, #6f5650 45%, var(--photo-b) 100%);
    clip-path: polygon(0 0, 100% 31px, 100% 100%, 0 389px);
  }
  .headline {
    position: absolute; left: 49px; top: 194px;
    color: var(--navy); font-weight: 700; font-size: 80px; line-height: 78px;
    letter-spacing: 0.5px; text-transform: uppercase;
  }
  .perks {
    position: absolute; left: 49px; top: 580px;
    color: var(--ink); font-weight: 300; font-size: 33px; line-height: 42px;
  }
  .perks strong { color: var(--navy); font-weight: 700; }
  .topics {
    position: absolute; left: 0; top: 673px; width: 792px; height: 447px;
    background: var(--navy-deep); padding: 34px 72px 0 49px;
    list-style: none; color: var(--white);
  }
  .topic { margin-bottom: 20px; }
  .topic-title {
    font-weight: 600; font-size: 24px; line-height: 30px; text-transform: uppercase;
    letter-spacing: 0.3px; display: flex;
  }
  .topic-title::before { content: ">"; width: 30px; padding-left: 3px; font-weight: 500; }
  .topic-text { font-weight: 300; font-size: 18px; line-height: 23px; }
</style>
</head>
<body>
  <main class="flyer">
    <div class="brand brand-financial"><span class="brand-mark"></span><span>Quelmora<br>Financial</span></div>
    <div class="brand brand-law">PWR Law</div>
    <div class="accent-bar"></div>
    <div class="speaker-photo" role="img" aria-label="Photo of Renata and Dan Volkhaven seated together in front of a brick building"></div>

    <h1 class="headline">Estate &amp;<br>Financial<br>Planning<br>Essentials</h1>

    <p class="perks">Food will be provided,<br>Raffle for <strong>$500</strong> off an Estate Plan Package</p>

    <ul class="topics">
      <li class="topic">
        <h2 class="topic-title">Protect Your Future</h2>
        <p class="topic-text">Build a strong financial foundation with emergency funds, retirement planning, and smart investment strategies that match your goals.</p>
      </li>
      <li class="topic">
        <h2 class="topic-title">Secure Your Legacy</h2>
        <p class="topic-text">Learn about wills, trusts, and powers of attorney - the essential documents everyone needs to protect their family's future.</p>
      </li>
      <li class="topic">
        <h2 class="topic-title">Guard Your Assets</h2>
        <p class="topic-text">Understand the right insurance coverage to protect yourself and your loved ones, from life insurance to long-term care options.</p>
      </li>
      <li class="topic">
        <h2 class="topic-title">Transfer Wealth Wisely</h2>
        <p class="topic-text">Discover tax-efficient strategies for passing assets to the next generation and making the most of your charitable giving.</p>
      </li>
    </ul>
  </main>
</body>
</html>
```